Copperfox Billboard

Please design a billboard using my photos and logos.
For photo of truck please crop the truck itself out and not have the trees / dirt in photo.
Please put " Best Prices in Sevier County"
Please put " 30-yard Dumpsters Starting at 600.00"
Please put " 16-yard Dumpsters Starting at 300.0"
Please put " Delivery and Pickup 7 Days a week"
Billboard size will be 10 ft tall 30 ft wide

```html
<!DOCTYPE html>
<html lang="en">
<head>
<meta charset="utf-8">
<title>Copperfox Dumpsters Billboard</title>
<link rel="stylesheet" href="https://fonts.googleapis.com/css2?family=Poppins:wght@600;700;800&display=swap">
<style>
  :root {
    --ink: #070708;
    --charcoal: #231f20;
    --purple: #7b3fa0;
    --purple-deep: #3a1650;
    --white: #ffffff;
    --paper: #f1f1f1;
    --rule: #3b2a47;
  }
  html, body {
    margin: 0;
    padding: 0;
    width: 779px;
    height: 1200px;
    overflow: hidden;
    background: var(--white);
  }
  .billboard {
    position: absolute;
    left: 25px;
    top: 35px;
    width: 729px;
    height: 243px;
    overflow: hidden;
    background: var(--ink);
    font-family: "Poppins", sans-serif;
  }
  .billboard__shapes {
    position: absolute;
    inset: 0;
  }
  .truck-photo {
    position: absolute;
    left: 412px;
    top: 38px;
    width: 304px;
    height: 166px;
    border-radius: 6px;
    background: linear-gradient(100deg, #e9e9ec 0%, #cfd0d4 45%, #4a2a66 70%, #2b1740 100%);
  }
  .brand {
    position: absolute;
    left: 40px;
    top: 12px;
    width: 315px;
    margin: 0;
    text-align: center;
    color: var(--white);
    font-weight: 700;
    text-transform: uppercase;
    line-height: 1;
  }
  .brand__name { display: block; font-size: 38px; letter-spacing: 1px; }
  .brand__sub { display: block; font-size: 20px; letter-spacing: 2px; margin-top: 2px; padding-left: 80px; }
  .divider {
    position: absolute;
    left: 40px;
    top: 98px;
    width: 315px;
    height: 1px;
    background: var(--rule);
  }
  .offers {
    position: absolute;
    left: 0;
    top: 99px;
    width: 395px;
    margin: 0;
    padding: 0;
    list-style: none;
    text-align: center;
    color: var(--white);
    font-weight: 600;
  }
  .offers__item { font-size: 18.5px; line-height: 25.5px; }
  .offers__item--lead { font-size: 17.5px; }
  .hours {
    position: absolute;
    left: 15px;
    top: 183px;
    margin: 0;
    font-family: "Poppins", sans-serif;
    font-weight: 800;
    font-size: 13.5px;
    line-height: 20px;
    color: var(--ink);
    letter-spacing: 1.4px;
    white-space: nowrap;
  }
  .hours__accent { color: var(--purple); }
  .phone {
    position: absolute;
    left: 14px;
    top: 206px;
    display: flex;
    align-items: center;
    gap: 3px;
    color: var(--white);
    font-weight: 600;
    font-size: 30px;
    line-height: 36px;
    letter-spacing: 0.5px;
  }
  .web {
    position: absolute;
    left: 257px;
    top: 213px;
    display: flex;
    align-items: center;
    gap: 4px;
    color: var(--white);
    font-weight: 600;
    font-size: 15px;
    line-height: 22px;
  }
  .web__tld { color: var(--purple); }
</style>
</head>
<body>
  <section class="billboard">
    <svg class="billboard__shapes" width="729" height="243" viewBox="0 0 729 243">
      <defs>
        <linearGradient id="panel-purple" x1="0" y1="0" x2="1" y2="1">
          <stop offset="0" stop-color="#2a0f3a"/>
          <stop offset="0.45" stop-color="#7b3fa0"/>
          <stop offset="1" stop-color="#1c0a28"/>
        </linearGradient>
      </defs>
      <polygon points="469,0 612,0 729,200 729,243 588,243" fill="var(--paper)"/>
      <polygon points="585,0 729,0 729,243 720,243" fill="url(#panel-purple)"/>
      <rect x="0" y="180" width="400" height="25" fill="var(--white)"/>
      <polygon points="0,205 588,205 588,243 0,243" fill="var(--charcoal)"/>
      <polygon points="540,205 570,205 588,243 560,243" fill="var(--purple-deep)"/>
      <polygon points="0,205 247,205 262,243 0,243" fill="var(--purple)"/>
    </svg>

    <div class="truck-photo" role="img" aria-label="Photo of a white roll-off truck carrying a purple dumpster"></div>

    <h1 class="brand">
      <span class="brand__name">Copperfox</span>
      <span class="brand__sub">Dumpsters</span>
    </h1>
    <div class="divider"></div>

    <ul class="offers">
      <li class="offers__item offers__item--lead">Best Prices in Sevier County</li>
      <li class="offers__item">30-yard Dumpsters Starting at 600.00</li>
      <li class="offers__item">16-yard Dumpsters Starting at 300.0</li>
    </ul>

    <p class="hours"><span class="hours__accent">DELIVERY</span> AND <span class="hours__accent">PICKUP</span> 7 <span class="hours__accent">DAYS</span> A <span class="hours__accent">WEEK</span></p>

    <div class="phone">
      <svg width="22" height="22" viewBox="0 0 24 24" aria-hidden="true">
        <path d="M6.6 3.5l2.6 3.2-1.6 2.2c1.3 2.7 3.4 4.8 6.1 6.1l2.2-1.6 3.2 2.6-1.4 3c-7.5-.4-13.5-6.4-13.900-13.900z" fill="none" stroke="var(--white)" stroke-width="1.8" stroke-linejoin="round"/>
        <path d="M14 3.5a6.5 6.5 0 0 1 6.5 6.5M14 7a3 3 0 0 1 3 3" fill="none" stroke="var(--white)" stroke-width="1.6" stroke-linecap="round"/>
      </svg>
      <span class="phone__number">865 555 0142</span>
    </div>

    <div class="web">
      <svg width="20" height="20" viewBox="0 0 24 24" aria-hidden="true">
        <g fill="none" stroke="var(--purple)" stroke-width="1.5">
          <circle cx="12" cy="12" r="10"/>
          <ellipse cx="12" cy="12" rx="4.5" ry="10"/>
          <path d="M2 12h20M4 6.5h16M4 17.5h16"/>
        </g>
      </svg>
      <span>copperfoxdumpsters<span class="web__tld">.com</span></span>
    </div>
  </section>
</body>
</html>
```